Gutscheinkarte aus Plastik
Zielgruppe
Fitnessbekleidung, Sportbekleidung, Funktionsbekleidung,Gym,Onlineshop,
Aufgabenstellung
Erstellen einer Gutscheinkarte aus Plastik für unseren neuen Onlineshop, die bei Bestellungen mit an die Kunden versendet wird.
-Maße: 86x54mm
-Farben: Schwarz und Neongrün(c0e200) evtl. noch eine dritte Farbe (wird Designer überlassen)
Folgender Text sollte vorhanden sein (Vorderseite):
Gutscheinwert: 10€
Gutscheincode: Ascend
Gültig: ab einem Bestellwert von 75€
Webadresse: www.ascend-now-sports.de
Unsere Marken: s. Anlage
Bitte Reihenfolge beigehalten + uvm.
Rückseite:
Versand in folgende Länder (evtl mit Länderflaggen oder Europakarte mit Stecknadel in der Ländern):
Deutschland
Österreich
Frankreich
Italien
Großbritannien
Niederlande
Belgien
Bulgarien
Dänemark
Estland
Finnland
Griechenland
Irland
Lettland
Litauen
Luxemburg
Malta
Polen
Portugal
Rumänien
Schweden
Slowakei
Slowenien
Spanien
Tschechien
Ungarn
Zypern

```html
<!DOCTYPE html>
<html lang="de">
<head>
<meta charset="utf-8">
<title>Gutscheinkarte – Ascend</title>
<link rel="stylesheet" href="https://fonts.googleapis.com/css2?family=PT+Sans+Narrow:wght@700&family=Source+Sans+3:wght@400;600&display=swap">
<style>
  :root {
    --stage: #050606;
    --card-dark: #232323;
    --card-green: #2f6a4a;
    --card-green-deep: #1d3f2e;
    --neon: #c0e200;
    --neon-deep: #6f8f00;
    --ink-dark: #2a2f10;
    --text-light: #ffffff;
    --text-soft: #e6e6e6;
  }
  * { margin: 0; padding: 0; box-sizing: border-box; }
  html, body { width: 1200px; height: 848px; overflow: hidden; }
  body {
    position: relative;
    background: var(--stage);
    font-family: "Source Sans 3", "Myriad Pro", sans-serif;
    color: var(--text-light);
  }
  .card {
    position: absolute;
    width: 425px;
    height: 676px;
    overflow: hidden;
    background: var(--card-dark);
  }
  .card--front { left: 166px; top: 38px; }
  .card--back { left: 646px; top: 121px; }

  .card__texture {
    position: absolute;
    inset: 0;
  }
  .card--front .card__texture {
    background:
      linear-gradient(160deg, rgba(47,106,74,0.55) 0%, rgba(35,35,35,0) 38%),
      linear-gradient(20deg, rgba(35,35,35,1) 35%, rgba(47,106,74,0.55) 60%, rgba(35,35,35,0.9) 85%);
  }
  .card--back .card__texture {
    background:
      linear-gradient(180deg, rgba(47,106,74,0.85) 0%, rgba(29,63,46,0.6) 20%, rgba(35,35,35,1) 32%, rgba(35,35,35,1) 80%, rgba(29,63,46,0.7) 100%);
  }

  .voucher-value {
    position: absolute;
    left: 0; right: 0;
    top: 186px;
    text-align: center;
    font-family: "PT Sans Narrow", "Myriad Pro Condensed", sans-serif;
    font-weight: 700;
    font-size: 196px;
    line-height: 1;
    letter-spacing: -6px;
    background: linear-gradient(180deg, var(--neon) 30%, var(--neon-deep) 100%);
    -webkit-background-clip: text;
    background-clip: text;
    color: transparent;
  }
  .code-ribbon {
    position: absolute;
    left: 54px;
    top: 352px;
    width: 334px;
    height: 72px;
  }
  .code-ribbon__label {
    position: absolute;
    left: 0; right: 0;
    top: 8px;
    text-align: center;
    font-family: "Source Sans 3", sans-serif;
    font-weight: 600;
    font-size: 44px;
    line-height: 1;
    color: var(--ink-dark);
  }
  .shop-url {
    position: absolute;
    left: 0; right: 0;
    top: 558px;
    padding-left: 52px;
    text-align: center;
    font-size: 25px;
    font-weight: 600;
    color: var(--neon-deep);
    background: linear-gradient(180deg, var(--neon) 20%, var(--neon-deep) 100%);
    -webkit-background-clip: text;
    background-clip: text;
    color: transparent;
  }
  .validity {
    position: absolute;
    left: 0; right: 0;
    top: 592px;
    padding-left: 52px;
    text-align: center;
    font-size: 15px;
    color: var(--text-soft);
  }
  .brand-row {
    position: absolute;
    left: 26px; right: 26px;
    top: 648px;
    display: flex;
    justify-content: space-between;
    align-items: center;
    font-size: 15px;
    font-weight: 600;
    color: var(--text-light);
    transform: translateY(-30px);
  }

  .shipping-title {
    position: absolute;
    left: 0; right: 0;
    top: 128px;
    text-align: center;
    font-family: "PT Sans Narrow", sans-serif;
    font-weight: 700;
    font-size: 37px;
    line-height: 39px;
    color: var(--neon);
    text-shadow: 0 2px 3px rgba(0,0,0,0.7);
  }
  .country-list {
    position: absolute;
    left: 0; right: 0;
    top: 232px;
    list-style: none;
    text-align: center;
    font-size: 26px;
    line-height: 29.8px;
    color: var(--text-light);
  }
</style>
</head>
<body>
  <section class="card card--front" aria-label="Gutscheinkarte Vorderseite">
    <div class="card__texture" role="img" aria-label="Dunkles geometrisches Dreiecksmuster in Grün und Anthrazit"></div>
    <div class="voucher-value">10€</div>
    <div class="code-ribbon">
      <svg width="334" height="72" viewBox="0 0 334 72" aria-hidden="true">
        <polygon points="0,2 40,2 40,52 0,52 14,27" fill="#a8c400"/>
        <polygon points="294,20 334,20 320,45 334,70 294,70" fill="#7f9a00"/>
        <polygon points="38,0 294,14 294,62 40,58" fill="#000" opacity="0.25"/>
        <rect x="38" y="8" width="256" height="52" fill="#b5d400"/>
        <rect x="38" y="8" width="256" height="52" fill="none" stroke="#1e2408" stroke-width="1.5"/>
      </svg>
      <div class="code-ribbon__label">Code: Ascend</div>
    </div>
    <div class="shop-url">www.ascend-now-sports.de</div>
    <div class="validity">Gültig: Ab einem Bestellwert von 75€</div>
    <div class="brand-row">
      <span class="brand-name">Ironvale</span>
      <span class="brand-name">Stridecore</span>
      <span class="brand-name">Bulkline</span>
      <span class="brand-name">Forthmove</span>
      <span class="brand-name">Kelvo</span>
    </div>
  </section>

  <section class="card card--back" aria-label="Gutscheinkarte Rückseite">
    <div class="card__texture" role="img" aria-label="Dunkles geometrisches Dreiecksmuster in Grün und Anthrazit"></div>
    <h2 class="shipping-title">VERSAND IN<br>FOLGENDE LÄNDER:</h2>
    <ul class="country-list">
      <li>Deutschland · Österreich</li>
      <li>Frankreich · Italien</li>
      <li>Großbritannien · Niederlande</li>
      <li>Belgien · Bulgarien · Dänemark</li>
      <li>Estland · Finnland · Griechenland</li>
      <li>Irland · Lettland · Litauen</li>
      <li>Luxemburg · Malta</li>
      <li>Polen · Portugal · Rumänien</li>
      <li>Schweden · Slowakei</li>
      <li>Slowenien · Spanien</li>
      <li>Tschechien · Ungarn · Zypern</li>
    </ul>
  </section>
</body>
</html>
```